OAKandRIVER Learning & Development
Business card, Letterhead & Compliment Slip design
Simple
Mara Hollings
Director
41 Fennick Row
Taplow
South Bucks KX4 7RB
mhollings@oakandriverltd-example.co.uk
www.oakandriverltd-example.co.uk
Letterhead needs to be UK standard size A4 and used electronically, therefore, not too heavy on printer toner.
Compliment slip needs to be DL size which is 110mm x 220mm.
We are open to your ideas on this, it could be that the logo is on the front and all other details on reverse side.
We would like to see your ideas please.
Please see attached file for our logo, to be included in this design project. Many thanks.

```html
<!DOCTYPE html>
<html lang="en">
<head>
<meta charset="utf-8">
<title>Oak and River Stationery Set</title>
<link href="https://fonts.googleapis.com/css2?family=Montserrat:ital,wght@0,300;0,400;0,600;1,300&display=swap" rel="stylesheet">
<style>
  :root {
    --backdrop: #4b3e36;
    --ink: #111111;
    --paper: #f7f7f7;
    --paper-shade: #e4e4e4;
    --gold: #c9a24a;
    --text-light: #e8e8e8;
    --text-dark: #1a1a1a;
    --text-muted: #8a8a8a;
    --rule: #c8c8c8;
  }
  * { box-sizing: border-box; margin: 0; padding: 0; }
  html, body { width: 1200px; height: 571px; overflow: hidden; }
  body {
    background: var(--backdrop);
    font-family: "Montserrat", Arial, sans-serif;
    position: relative;
  }
  .piece { position: absolute; box-shadow: 0 3px 8px rgba(0,0,0,.45); overflow: hidden; }

  .wordmark {
    display: flex; align-items: center; gap: 4px;
    color: var(--gold); font-weight: 400; letter-spacing: .3px; white-space: nowrap;
  }
  .wordmark .dot { border-radius: 50%; background: var(--gold); flex: none; }
  .wordmark-lg { font-size: 11px; flex-direction: column; gap: 4px; }
  .wordmark-lg .dot { width: 12px; height: 12px; }
  .wordmark-sm { font-size: 8px; flex-direction: column; gap: 3px; }
  .wordmark-sm .dot { width: 9px; height: 9px; }
  .wordmark-row { flex-direction: row; font-size: 8px; gap: 5px; }
  .wordmark-row .dot { width: 8px; height: 8px; }

  /* business cards */
  .card { border-radius: 6px; }
  .card-dark { background: var(--ink); color: var(--text-light); }
  .card-light { background: linear-gradient(180deg, var(--paper), var(--paper-shade)); }
  .card .centered { position: absolute; inset: 0; display: flex; align-items: center; justify-content: center; }
  .card .holder { position: absolute; left: 14px; top: 14px; font-size: 6px; color: var(--gold); }
  .card .holder strong { display: block; font-weight: 600; font-size: 9px; color: var(--text-light); margin-bottom: 2px; }
  .card .contact { position: absolute; left: 14px; bottom: 12px; font-size: 5px; line-height: 1.5; color: #bdbdbd; }
  .card .gold-rule { position: absolute; left: 0; right: 0; height: 1.5px; background: var(--gold); }
  .card-split { background: var(--ink); }
  .card-split .logo-side { position: absolute; left: 0; top: 0; bottom: 0; width: 54%; display: flex; align-items: center; justify-content: center; }
  .card-split .white-side { position: absolute; right: 0; top: 0; bottom: 0; width: 46%; background: var(--paper); }
  .card-split .white-side .holder { left: 8px; top: 10px; font-size: 5px; }
  .card-split .white-side .holder strong { font-size: 6px; color: var(--text-dark); }

  /* letterheads */
  .letterhead { background: var(--paper); }
  .letterhead .header-band {
    height: 50px; background: var(--ink); display: flex; align-items: center; padding-left: 14px;
    border-bottom: 2px solid var(--gold);
  }
  .letterhead .footer-text {
    position: absolute; left: 0; right: 0; bottom: 8px; text-align: center;
    font-size: 4.5px; color: var(--text-muted); line-height: 1.6;
  }
  .letterhead .footer-rule { position: absolute; left: 14px; right: 14px; bottom: 24px; height: 1px; background: var(--gold); }
  .fax-form { position: absolute; left: 14px; right: 14px; top: 66px; font-size: 5px; color: #555; }
  .fax-form .field { display: flex; align-items: flex-end; gap: 6px; margin-bottom: 7px; }
  .fax-form .field b { width: 22px; font-weight: 400; }
  .fax-form .field i { flex: 1; border-bottom: 1px solid var(--rule); }
  .fax-form .checks { display: flex; justify-content: space-between; margin-top: 10px; }
  .fax-form .checks span::before {
    content: ""; display: inline-block; width: 5px; height: 5px; border: 1px solid #888; margin-right: 3px; vertical-align: middle;
  }
  .fax-form .divider { height: 1px; background: var(--rule); margin-top: 8px; }

  /* envelope & slip */
  .envelope { background: var(--paper); }
  .envelope .flap { position: absolute; left: 0; top: 0; width: 100%; height: 50px; }
  .envelope .flap-mark { position: absolute; left: 0; right: 0; top: 8px; display: flex; justify-content: center; }
  .envelope .return-line { position: absolute; left: 0; right: 0; top: 53px; text-align: center; font-size: 4.5px; color: var(--text-muted); }

  .slip { background: var(--paper); }
  .slip .header-band { height: 30px; background: var(--ink); border-bottom: 2px solid var(--gold); display: flex; align-items: center; padding-left: 12px; }
  .slip .compliments {
    position: absolute; right: 16px; bottom: 16px; font-style: italic; font-weight: 300;
    font-size: 13px; color: #333;
  }
  .slip .footer-text { position: absolute; left: 12px; bottom: 6px; font-size: 4.5px; color: var(--text-muted); }
</style>
</head>
<body>

  <!-- business cards -->
  <div class="piece card card-split" style="left:149px;top:48px;width:120px;height:100px;">
    <div class="logo-side"><div class="wordmark wordmark-sm"><span class="dot"></span>Oak and River</div></div>
    <div class="white-side">
      <div class="holder"><strong>Mara Hollings</strong>Director</div>
    </div>
  </div>

  <div class="piece card card-light" style="left:96px;top:156px;width:132px;height:103px;">
    <div class="centered"><div class="wordmark wordmark-lg"><span class="dot"></span>Oak and River</div></div>
  </div>

  <div class="piece card card-dark" style="left:232px;top:156px;width:176px;height:103px;">
    <div class="centered"><div class="wordmark wordmark-lg"><span class="dot"></span>Oak and River</div></div>
  </div>

  <div class="piece card card-dark" style="left:115px;top:300px;width:122px;height:96px;">
    <div class="centered"><div class="wordmark wordmark-sm"><span class="dot"></span>Oak and River</div></div>
    <div class="gold-rule" style="bottom:14px;"></div>
  </div>

  <div class="piece card card-dark" style="left:241px;top:300px;width:172px;height:96px;">
    <div class="holder"><strong>Mara Hollings</strong>Director</div>
    <div class="contact">41 Fennick Row, Taplow, South Bucks KX4 7RB<br>mhollings@oakandriverltd-example.co.uk<br>www.oakandriverltd-example.co.uk</div>
    <div class="gold-rule" style="bottom:6px;"></div>
  </div>

  <div class="piece card card-dark" style="left:132px;top:413px;width:120px;height:91px;">
    <div class="holder" style="font-size:5px;"><strong style="font-size:7px;">Mara Hollings</strong>Director</div>
    <div class="contact" style="font-size:4px;">41 Fennick Row<br>Taplow, South Bucks KX4 7RB<br>mhollings@oakandriverltd-example.co.uk</div>
  </div>

  <!-- letterhead -->
  <div class="piece letterhead" style="left:427px;top:43px;width:240px;height:365px;">
    <div class="header-band"><div class="wordmark wordmark-sm"><span class="dot"></span>Oak and River</div></div>
    <div class="footer-rule"></div>
    <div class="footer-text">OAKandRIVER Learning &amp; Development · 41 Fennick Row, Taplow, South Bucks KX4 7RB<br>mhollings@oakandriverltd-example.co.uk · www.oakandriverltd-example.co.uk</div>
  </div>

  <!-- fax / form sheet -->
  <div class="piece letterhead" style="left:684px;top:43px;width:240px;height:365px;">
    <div class="header-band"><div class="wordmark wordmark-sm"><span class="dot"></span>Oak and River</div></div>
    <div class="fax-form">
      <div class="field"><b>To:</b><i></i></div>
      <div class="field"><b>From:</b><i></i></div>
      <div class="field"><b>Re:</b><i></i></div>
      <div class="field"><b>Date:</b><i></i></div>
      <div class="field"><b>Pages:</b><i></i></div>
      <div class="checks"><span>Urgent</span><span>Review</span><span>Reply</span><span>Recycle</span></div>
      <div class="divider"></div>
    </div>
    <div class="footer-rule"></div>
    <div class="footer-text">OAKandRIVER Learning &amp; Development · 41 Fennick Row, Taplow, South Bucks KX4 7RB<br>mhollings@oakandriverltd-example.co.uk · www.oakandriverltd-example.co.uk</div>
  </div>

  <!-- envelope -->
  <div class="piece envelope" style="left:427px;top:420px;width:305px;height:120px;">
    <svg class="flap" viewBox="0 0 305 50" preserveAspectRatio="none">
      <polygon points="0,0 305,0 305,18 152.5,50 0,18" fill="#111111"/>
      <polyline points="0,18 152.5,50 305,18" fill="none" stroke="#c9a24a" stroke-width="1.5"/>
    </svg>
    <div class="flap-mark"><div class="wordmark wordmark-sm"><span class="dot"></span>Oak and River</div></div>
    <div class="return-line">41 Fennick Row, Taplow, South Bucks KX4 7RB</div>
  </div>

  <!-- compliment slip -->
  <div class="piece slip" style="left:749px;top:420px;width:331px;height:120px;">
    <div class="header-band"><div class="wordmark wordmark-row"><span class="dot"></span>Oak and River</div></div>
    <div class="compliments">With Compliments</div>
    <div class="footer-text">www.oakandriverltd-example.co.uk</div>
  </div>

</body>
</html>
```